Oil and Gas Company: Letterhead Design

In short we need a professional company letterhead designed for our Oil and Gas company.

We would like to keep the design simple and professional. Letterhead to include the company logo and color scheme, front page and continuation pages.

For reference, see attached logo below with our company logo and color scheme.

Target Market(s)

Oil & Gas Market

Industry/Entity Type

Oil And Gas

Font styles to use
Sans Serif

Requirements
Must have
• Letterhead must contain a front page & continuation page.
• Must be simple and professional in design.
• Follow our logo and color scheme.
Nice to have
• I would like to have the logo embedded in the bottom right hand portion of the page to provide some depth into the letterhead.

```html
<!DOCTYPE html>
<html lang="en">
<head>
<meta charset="utf-8">
<title>Ardent Ridge Energy – Letterhead Set</title>
<link href="https://fonts.googleapis.com/css2?family=Lato:wght@400;700&display=swap" rel="stylesheet">
<style>
  :root {
    --backdrop: #d1d2d4;
    --paper: #ffffff;
    --brand-red: #e31e26;
    --brand-blue: #1456a5;
    --ink: #1a1a1a;
    --label-ink: #231f20;
  }
  * { margin: 0; padding: 0; box-sizing: border-box; }
  html, body { width: 1200px; height: 1200px; overflow: hidden; }
  body {
    background: var(--backdrop);
    font-family: "Lato", Arial, sans-serif;
    position: relative;
  }
  .sheet {
    position: absolute;
    top: 264px;
    width: 476px;
    height: 673px;
    background: var(--paper);
    box-shadow: 2px 2px 3px rgba(0,0,0,0.18);
  }
  .sheet--front { left: 94px; }
  .sheet--continuation { left: 628px; }
  .sheet__band {
    position: absolute;
    left: 0; bottom: 0;
    width: 476px; height: 13px;
    display: block;
  }
  .sheet__tagline {
    position: absolute;
    left: 33px;
    top: 643px;
    font-size: 6px;
    font-weight: 700;
    letter-spacing: 0.1px;
    color: var(--ink);
    text-transform: uppercase;
  }
  .brand-name {
    position: absolute;
    right: 30px;
    top: 628px;
    display: flex;
    align-items: center;
    gap: 5px;
    font-size: 11px;
    font-weight: 700;
    color: var(--brand-blue);
    white-space: nowrap;
  }
  .brand-name__square {
    width: 9px; height: 9px;
    background: var(--brand-red);
  }
  .sheet-label {
    position: absolute;
    top: 972px;
    width: 476px;
    text-align: center;
    font-size: 15px;
    letter-spacing: 3px;
    color: var(--label-ink);
  }
  .sheet-label--front { left: 94px; }
  .sheet-label--continuation { left: 628px; }
</style>
</head>
<body>

  <section class="sheet sheet--front" aria-label="Letterhead front page">
    <div class="brand-name"><span class="brand-name__square"></span>Ardent Ridge Energy</div>
    <p class="sheet__tagline">Petroleum Oilfield Services</p>
    <svg class="sheet__band" viewBox="0 0 476 13" preserveAspectRatio="none" aria-hidden="true">
      <polygon points="0,0 386,0 380,13 0,13" fill="var(--brand-red)"/>
      <polygon points="389,0 476,0 476,13 383,13" fill="var(--brand-blue)"/>
    </svg>
  </section>

  <section class="sheet sheet--continuation" aria-label="Continuation page">
    <svg class="sheet__band" viewBox="0 0 476 13" preserveAspectRatio="none" aria-hidden="true">
      <polygon points="0,0 388,0 382,13 0,13" fill="var(--brand-red)"/>
      <polygon points="391,0 476,0 476,13 385,13" fill="var(--brand-blue)"/>
    </svg>
  </section>

  <p class="sheet-label sheet-label--front">Letterhead</p>
  <p class="sheet-label sheet-label--continuation">Continuation page</p>

</body>
</html>
```